Plastic Aesthetic and Reconstructive Surgery

I need a double sided luxurius Business Card, with a minimal, modern design focused on my job.
Besides my Name, Surname and contact information, the use of my initials (M and T) in free style combination as a logo will help.
In the one side all data written in English.
In the other side written in Greek if possible.
Please feel free to use the letter type and size you prefer.
Please use icons type and size and orientation you like.
The Name, Surname, occupation and the initials can be UV spotted.
You can use also in the background a texture or something that will make the card luxurious.
I would prefer pal colors.
Each side can have different colors or even better they can be reversed or inverted
As I have said you can use the wet sand color, light brown, dark brown, gold, light gold, white
Updates

Need extra days to review

i am waiting for some new ideas and some modifications from the designers. I need a couple of days extention of the period for the designers to post their modifications.

Target Market(s)

Patients who need a reconstructive intervention or surgery. Also people, mainly women, that they need aesthetic or cosmetic interventions to face or body

Contact Information for Business Card

Name and surname, occupation, member of an organization , mobile telephone number, Mail, Facebook and Instagram accounts

Font styles to use
Script
Other font styles liked:
• Gabriola

Colors
FFC000
F8CF3A
FAE287
FDF2CF
FEFAEE

Requirements
Must have
• A free combination of my initials (M and T) as a logo
Nice to have
• Fade out with the background colors, UV spotted of the name, initials logo
Should not have
• Address

```html
<!DOCTYPE html>
<html lang="en">
<head>
<meta charset="utf-8">
<title>Markos Theodorou – Business Card</title>
<link href="https://fonts.googleapis.com/css2?family=Marcellus&family=Poppins:wght@300;400;600&display=swap" rel="stylesheet">
<style>
  :root {
    --backdrop: #e6e6e6;
    --kraft: #c9a583;
    --ink: #0b1116;
    --blush: #d9b59a;
    --paper: #ffffff;
    --text-grey: #444444;
  }
  * { box-sizing: border-box; margin: 0; padding: 0; }
  html, body { width: 1200px; height: 1085px; overflow: hidden; }
  body { background: var(--backdrop); position: relative; font-family: "Poppins", sans-serif; }

  .card { position: absolute; left: 300px; width: 580px; height: 343px; }
  .card--front { top: 163px; background: var(--kraft); color: var(--ink); text-align: center; }
  .card--back { top: 559px; background: var(--paper); }

  .front__monogram {
    position: absolute; left: 0; right: 0; top: 48px;
    font-family: "Marcellus", serif; font-size: 150px; line-height: 1; color: var(--ink);
  }
  .front__name {
    position: absolute; left: 0; right: 0; top: 238px;
    font-family: "Marcellus", serif; font-size: 25px; letter-spacing: -0.3px;
  }
  .front__role {
    position: absolute; left: 0; right: 0; top: 270px;
    font-weight: 600; font-size: 14.5px;
  }

  .back__monogram {
    position: absolute; left: 30px; top: 28px;
    font-family: "Marcellus", serif; font-size: 112px; line-height: 1; color: var(--blush);
  }
  .back__name {
    position: absolute; left: 175px; top: 130px;
    font-weight: 300; font-size: 18.5px; color: var(--blush); white-space: nowrap;
  }
  .back__role {
    position: absolute; left: 175px; top: 155px;
    font-weight: 300; font-size: 13.5px; color: var(--text-grey); white-space: nowrap;
  }
  .rule { position: absolute; left: 178px; width: 97px; height: 1px; background: var(--blush); }
  .rule--top { top: 191px; }
  .rule--bottom { top: 266px; }
  .contact {
    position: absolute; left: 178px; display: flex; align-items: center; gap: 9px;
    font-size: 17px; color: var(--text-grey); white-space: nowrap;
  }
  .contact--phone { top: 205px; }
  .contact--mail { top: 226px; }
  .contact svg { width: 17px; height: 14px; }
  .social {
    position: absolute; left: 178px; top: 280px; display: flex; align-items: center; gap: 6px;
    font-size: 14px; color: var(--blush);
  }
  .social__dot { width: 10px; height: 10px; border-radius: 50%; background: var(--blush); }
</style>
</head>
<body>
  <section class="card card--front" aria-label="Card front, English">
    <div class="front__monogram">MT</div>
    <div class="front__name">Markos Theodorou, MD, MSc</div>
    <div class="front__role">Plastic Reconstructive and Aesthetic Surgery</div>
  </section>

  <section class="card card--back" aria-label="Card back, Greek">
    <div class="back__monogram">MT</div>
    <div class="back__name">Μάρκος Θεοδώρου, MD, MSc</div>
    <div class="back__role">Αισθητική και Επανορθωτική Πλαστική Χειρουργική</div>
    <div class="rule rule--top"></div>
    <div class="contact contact--phone">
      <svg viewBox="0 0 24 20" aria-hidden="true"><path d="M6 2 L9 6 L7 8 C8 11 10 13 13 14 L15 12 L19 15 L17 18 C10 18 4 12 4 4 Z" fill="none" stroke="#d9b59a" stroke-width="1.8" stroke-linejoin="round"/></svg>
      <span>+30 690 218 4406</span>
    </div>
    <div class="contact contact--mail">
      <svg viewBox="0 0 24 17" aria-hidden="true"><rect x="0" y="0" width="24" height="17" fill="#d9b59a"/><path d="M0 0 L12 9 L24 0" fill="none" stroke="#fff" stroke-width="1.5"/></svg>
      <span>m.theodorou.clinic@mailbox.gr</span>
    </div>
    <div class="rule rule--bottom"></div>
    <div class="social"><span class="social__dot"></span><span>@dr.theodorou</span></div>
  </section>
</body>
</html>
```